Networking Diagram Graphic - Parallel, Distributed Computing/Storage Clusters

Hi. I need a high-level network diagram that depicts massively parallel and distributed computing/storage clusters within and between data centers. In addition to the basics such as servers and storage arrays, the diagram should include an icon that represents the software stack involved with accessing data from memory and storage. Depicting redundancy would be helpful as well. Please feel free to include any additional information/nodes you feel would be helpful.Time is of the essence and is more important than aesthetics. I am not looking for a finished product. Rather, I am interested in the concept for my team to review. Our ultimate goal is to identify the limitations of today's computing architecture.
Thanks.
Target Market(s)
IT, Data Centers, Servers, Storage
Industry/Entity Type
It Company
Colors
Look and feel

```html
<!DOCTYPE html>
<html lang="en">
<head>
<meta charset="utf-8">
<title>Parallel, Distributed Computing/Storage Clusters</title>
<link rel="stylesheet" href="https://fonts.googleapis.com/css2?family=Bowlby+One&display=swap">
<style>
  :root {
    --band: #fcad02;
    --paper: #f5f5f5;
    --title: #ffffff;
    --wire: #5a5a5a;
    --frame: #4b4b5c;
    --frame-base: #b9bcc6;
    --accent: #f4511e;
    --screen-blue: #4dd3f6;
    --bar-grey: #9a9aa5;
    --router-plate: #d5ebee;
    --router-body: #3a3a42;
    --led: #f9b208;
    --wave: #2fc7ec;
    --server: #5b6481;
    --server-dark: #424a63;
    --cloud: #5fa8f0;
    --db-top: #8fa9de;
    --db-mid: #6a7aa8;
    --db-low: #45506f;
  }
  html, body { margin: 0; padding: 0; overflow: hidden; }
  body { width: 1200px; height: 848px; background: var(--paper); }
  .diagram { display: block; width: 1200px; height: 848px; }
  .header-band { fill: var(--band); }
  .title {
    fill: var(--title);
    font-family: "Bowlby One", "Arial Black", sans-serif;
    font-size: 40px;
  }
  .wire { stroke: var(--wire); stroke-width: 1.2; fill: none; }
</style>
</head>
<body>
<svg class="diagram" viewBox="0 0 1500 1060" xmlns="http://www.w3.org/2000/svg">
  <defs>
    <symbol id="laptop" viewBox="0 0 100 70">
      <rect x="4" y="0" width="92" height="64" rx="4" fill="var(--frame)"/>
      <rect x="9" y="5" width="82" height="54" fill="#fff"/>
      <rect x="9" y="5" width="82" height="10" fill="var(--accent)"/>
      <rect x="14" y="9" width="10" height="2" fill="var(--led)"/>
      <circle cx="72" cy="10" r="1.3" fill="#fff"/><circle cx="77" cy="10" r="1.3" fill="#fff"/>
      <circle cx="82" cy="10" r="1.3" fill="#fff"/><circle cx="87" cy="10" r="1.3" fill="#fff"/>
      <rect x="14" y="22" width="28" height="27" fill="var(--screen-blue)"/>
      <rect x="46" y="22" width="32" height="3" fill="var(--accent)"/>
      <rect x="46" y="28" width="24" height="3" fill="var(--accent)"/>
      <rect x="46" y="34" width="14" height="2" fill="var(--bar-grey)"/><rect x="63" y="34" width="20" height="2" fill="var(--bar-grey)"/>
      <rect x="46" y="39" width="14" height="2" fill="var(--bar-grey)"/><rect x="63" y="39" width="20" height="2" fill="var(--bar-grey)"/>
      <rect x="46" y="44" width="14" height="2" fill="var(--bar-grey)"/><rect x="63" y="44" width="20" height="2" fill="var(--bar-grey)"/>
      <rect x="0" y="63" width="100" height="6" rx="2" fill="var(--frame-base)"/>
      <rect x="40" y="63" width="20" height="2" fill="var(--frame)"/>
    </symbol>
    <symbol id="router" viewBox="0 0 92 92">
      <rect x="0" y="53" width="92" height="38" fill="var(--router-plate)"/>
      <rect x="46" y="53" width="46" height="38" fill="#c7e2e6"/>
      <rect x="22" y="19" width="5" height="36" fill="var(--router-body)"/>
      <rect x="11" y="55" width="70" height="16" fill="var(--router-body)"/>
      <rect x="16" y="60" width="9" height="5" fill="var(--led)"/><rect x="32" y="60" width="9" height="5" fill="var(--led)"/>
      <rect x="48" y="60" width="9" height="5" fill="var(--led)"/><rect x="64" y="60" width="9" height="5" fill="var(--led)"/>
      <rect x="12" y="77" width="4" height="4" fill="#aac8cd"/><rect x="22" y="77" width="48" height="3" fill="#aac8cd"/><rect x="76" y="77" width="4" height="4" fill="#aac8cd"/>
      <path d="M38 14 a8 8 0 0 1 0 14" stroke="var(--wave)" stroke-width="4" fill="none" stroke-linecap="round"/>
      <path d="M45 7 a16 16 0 0 1 0 28" stroke="var(--wave)" stroke-width="4" fill="none" stroke-linecap="round"/>
      <path d="M52 1 a24 24 0 0 1 0 40" stroke="var(--wave)" stroke-width="4" fill="none" stroke-linecap="round"/>
    </symbol>
    <symbol id="monitor" viewBox="0 0 120 101">
      <rect x="0" y="0" width="120" height="84" rx="3" fill="var(--frame)"/>
      <rect x="5" y="5" width="110" height="66" fill="#fff"/>
      <rect x="0" y="74" width="120" height="10" fill="#d6d8de"/>
      <rect x="10" y="10" width="8" height="56" fill="var(--bar-grey)"/>
      <rect x="88" y="10" width="22" height="56" fill="#d3d5da"/>
      <rect x="31" y="12" width="22" height="22" fill="none" stroke="var(--accent)" stroke-width="3"/>
      <rect x="44" y="26" width="30" height="30" fill="none" stroke="var(--bar-grey)" stroke-width="1.5" stroke-dasharray="4 3"/>
      <path d="M53 30 l0 13 l3-3 l3 6 l2-1 l-3-6 l4 0z" fill="#222"/>
      <rect x="52" y="84" width="16" height="11" fill="#c4c7cf"/>
      <rect x="40" y="95" width="40" height="5" rx="2" fill="#b5b9c2"/>
    </symbol>
  </defs>

  <rect class="header-band" x="0" y="0" width="1500" height="218"/>
  <text class="title" x="756" y="122" text-anchor="middle" textLength="1258" lengthAdjust="spacingAndGlyphs">PARALLEL, DISTRIBUTED COMPUTING/STORAGE CLUSTERS</text>

  <g class="wiring">
    <path class="wire" d="M658 353H1273M818 353V385M1025 353V385M1273 353V385"/>
    <path class="wire" d="M591 392V453M591 548V612M202 513V635M268 687H537"/>
    <path class="wire" d="M650 682H1015M833 620V682M1015 620V682"/>
    <path class="wire" d="M1095 579H1157V876H967"/>
    <path class="wire" d="M193 756V878H318M392 878H455M455 813V943M455 813H573M455 943H573"/>
    <path class="wire" d="M708 813H781V943H708M781 880H845"/>
    <path class="wire" d="M907 925V1010H1273V472M1041 982V1010M1181 982V1010"/>
  </g>

  <g class="cloud-gateway">
    <path d="M160 410 a30 30 0 0 1 4-58 a38 38 0 0 1 70 4 a28 28 0 0 1 -4 54z" fill="var(--cloud)" stroke="#000" stroke-width="5"/>
    <path d="M171 412V370M160 382l11-12 11 12" stroke="#000" stroke-width="10" fill="none"/>
    <path d="M171 412V370M160 382l11-12 11 12" stroke="#f6b66c" stroke-width="5" fill="none"/>
    <path d="M211 362V404M200 392l11 12 11-12" stroke="#000" stroke-width="10" fill="none"/>
    <path d="M211 362V404M200 392l11 12 11-12" stroke="#f6b66c" stroke-width="5" fill="none"/>
    <rect x="150" y="421" width="82" height="19" rx="2" fill="var(--led)" stroke="#000" stroke-width="4"/>
    <rect x="160" y="429" width="50" height="3" fill="#000"/>
    <rect x="150" y="446" width="82" height="19" rx="2" fill="var(--led)" stroke="#000" stroke-width="4"/>
    <rect x="160" y="454" width="50" height="3" fill="#000"/>
    <rect x="150" y="472" width="82" height="19" rx="2" fill="var(--cloud)" stroke="#000" stroke-width="4"/>
    <rect x="160" y="480" width="50" height="3" fill="#000"/>
  </g>

  <g class="server-rack">
    <rect x="151" y="646" width="95" height="29" rx="4" fill="var(--server)"/>
    <rect x="151" y="677" width="95" height="29" rx="4" fill="var(--server-dark)"/>
    <rect x="151" y="708" width="95" height="31" rx="4" fill="var(--server)"/>
    <circle cx="167" cy="661" r="5" fill="#c9cfe0"/><circle cx="167" cy="692" r="5" fill="#c9cfe0"/><circle cx="167" cy="723" r="5" fill="#c9cfe0"/>
    <path d="M204 660h30M204 691h30" stroke="#c9cfe0" stroke-width="2" stroke-dasharray="2 3"/>
    <path d="M208 740 a10 10 0 0 1 2-19 a14 14 0 0 1 26 2 a9 9 0 0 1 2 17z" fill="var(--cloud)"/>
  </g>

  <g class="storage-db">
    <rect x="327" y="858" width="57" height="44" fill="var(--db-low)"/>
    <ellipse cx="355" cy="902" rx="28" ry="8" fill="var(--db-low)"/>
    <rect x="327" y="858" width="57" height="28" fill="var(--db-mid)"/>
    <ellipse cx="355" cy="886" rx="28" ry="8" fill="var(--db-mid)"/>
    <rect x="327" y="856" width="57" height="14" fill="var(--db-top)"/>
    <ellipse cx="355" cy="870" rx="28" ry="8" fill="var(--db-top)"/>
    <ellipse cx="355" cy="856" rx="28" ry="8" fill="#a7bdea"/>
    <path d="M367 882h20l-10 14 10 14h-20l10-14z" fill="#6fa7dc"/>
  </g>

  <use href="#router" x="545" y="292" width="92" height="92"/>
  <use href="#router" x="545" y="617" width="92" height="92"/>
  <use href="#router" x="862" y="822" width="92" height="92"/>

  <use href="#laptop" x="768" y="389" width="98" height="69"/>
  <use href="#laptop" x="976" y="389" width="98" height="69"/>
  <use href="#laptop" x="1224" y="389" width="98" height="69"/>
  <use href="#laptop" x="541" y="459" width="98" height="69"/>
  <use href="#laptop" x="791" y="540" width="98" height="69"/>
  <use href="#laptop" x="976" y="543" width="98" height="69"/>
  <use href="#laptop" x="992" y="899" width="98" height="69"/>
  <use href="#laptop" x="1132" y="899" width="98" height="69"/>

  <use href="#monitor" x="586" y="767" width="120" height="101"/>
  <use href="#monitor" x="586" y="912" width="120" height="101"/>
</svg>
</body>
</html>
```